Business card for law firm

Need business card for new law firm. Think confident, authoritative, conservative, but not stuffy or old-fashioned.

Contact Information for Business Card

Content for card - logo (uploaded), plus the following:

Paul Wexbury (larger font)
Managing Partner (larger font, but not as large as name)
Level 9, 41 Tansy Lane
Sydney NSW 2000
Main Tel 02 7346 2190
Direct Tel 02 6273 4415
Email paul@qvlegal.com.au
www.qvlegal.com.au

Letterhead design should include logo plus:
Level 9, 41 Tansy Lane
Sydney NSW 2000
Tel 02 6273 4415
www.qvlegal.com.au

```html
<!DOCTYPE html>
<html lang="en">
<head>
<meta charset="utf-8">
<title>Quillvale Legal – Business Card</title>
<link rel="stylesheet" href="https://fonts.googleapis.com/css2?family=EB+Garamond:wght@400;500&family=Roboto:wght@400&display=swap">
<style>
  :root {
    --backdrop: #d1d2d4;
    --card: #ffffff;
    --navy: #1f2557;
    --ink: #111111;
    --band: #000000;
  }
  * { box-sizing: border-box; margin: 0; padding: 0; }
  html, body {
    width: 1200px;
    height: 1200px;
    overflow: hidden;
    background: var(--backdrop);
  }
  .card {
    position: absolute;
    left: 267px;
    top: 410px;
    width: 666px;
    height: 381px;
    background: var(--card);
    overflow: hidden;
  }
  .brand {
    position: absolute;
    left: 21px;
    top: 24px;
    width: 170px;
    text-align: center;
  }
  .brand-mark {
    display: block;
    width: 38px;
    height: 38px;
    margin: 0 auto 22px;
    background: var(--navy);
  }
  .brand-name {
    font-family: "EB Garamond", serif;
    font-weight: 400;
    color: var(--navy);
    font-size: 24px;
    letter-spacing: 1.5px;
    line-height: 1;
    white-space: nowrap;
  }
  .person {
    position: absolute;
    left: 218px;
  }
  .person-name {
    top: 133px;
    font-family: "EB Garamond", serif;
    font-weight: 400;
    font-size: 43px;
    color: var(--navy);
    line-height: 1;
    white-space: nowrap;
  }
  .person-title {
    top: 197px;
    font-family: "Roboto", sans-serif;
    font-size: 24px;
    color: var(--ink);
    line-height: 1;
    white-space: nowrap;
  }
  .contact {
    position: absolute;
    font-family: "Roboto", sans-serif;
    font-size: 17.5px;
    color: var(--ink);
    line-height: 24px;
    white-space: nowrap;
  }
  .contact-icon { position: absolute; fill: var(--navy); }
  .contact-phone-text { left: 56px; top: 277px; }
  .contact-address-text { left: 241px; top: 279px; }
  .contact-email-text { left: 478px; top: 277px; }
  .contact-web-text { left: 477px; top: 309px; }
  .stripe-thin {
    position: absolute; left: 0; top: 354px; width: 100%; height: 4px; background: var(--band);
  }
  .stripe-thick {
    position: absolute; left: 0; top: 362px; width: 100%; height: 19px; background: var(--band);
  }
</style>
</head>
<body>
  <div class="card">
    <div class="brand">
      <span class="brand-mark"></span>
      <div class="brand-name">QUILLVALE LEGAL</div>
    </div>

    <div class="person person-name">Paul Wexbury</div>
    <div class="person person-title">Managing Partner</div>

    <svg class="contact-icon" style="left:22px;top:272px" width="21" height="32" viewBox="0 0 21 32" aria-hidden="true">
      <rect x="3" y="0" width="3" height="6" rx="1"/>
      <rect x="0" y="4" width="21" height="28" rx="5"/>
      <rect x="4" y="9" width="13" height="8" rx="1.5" fill="#fff"/>
      <circle cx="10.5" cy="25" r="2.2" fill="#fff"/>
    </svg>
    <div class="contact contact-phone-text">02 7346 2190<br>02 6273 4415</div>

    <svg class="contact-icon" style="left:206px;top:279px" width="24" height="33" viewBox="0 0 24 33" aria-hidden="true">
      <path d="M12 0C5.4 0 0 5.2 0 11.7 0 20 12 33 12 33s12-13 12-21.3C24 5.2 18.6 0 12 0z"/>
      <circle cx="12" cy="11.5" r="4.3" fill="#fff"/>
    </svg>
    <div class="contact contact-address-text">Level 9, 41 Tansy Lane<br>Sydney NSW 2000</div>

    <svg class="contact-icon" style="left:442px;top:282px" width="25" height="18" viewBox="0 0 25 18" aria-hidden="true">
      <rect x="1" y="1" width="23" height="16" fill="none" stroke="#1f2557" stroke-width="2"/>
      <path d="M1 1l11.5 9L24 1M1 17l8.5-8M24 17l-8.5-8" fill="none" stroke="#1f2557" stroke-width="2"/>
    </svg>
    <div class="contact contact-email-text">paul@qvlegal.com.au</div>

    <svg class="contact-icon" style="left:441px;top:309px" width="27" height="27" viewBox="0 0 27 27" aria-hidden="true">
      <g fill="none" stroke="#1f2557" stroke-width="2.2">
        <circle cx="12" cy="12" r="10.5"/>
        <ellipse cx="12" cy="12" rx="4.5" ry="10.5"/>
        <path d="M1.5 12h21M3.5 6.5h17M3.5 17.5h17"/>
      </g>
      <path d="M14 13l11 5-4.5 1.2 3.3 4.6-2 1.4-3.3-4.6-2.7 3.5z" stroke="#fff" stroke-width="1"/>
    </svg>
    <div class="contact contact-web-text">www.qvlegal.com.au</div>

    <div class="stripe-thin"></div>
    <div class="stripe-thick"></div>
  </div>
</body>
</html>
```